Relaunch of company website (Technical company)

Hi all,

we need a website based on Wordpress who makes the customer curious and excited of all the possibilities we can offer.
Customers are B2B. The layout should be based on the screenshots I added, but refreshed and modernized with some nice gadgets.
All needs to be responsive for the different devices.
We are a technical company. We provide a full range of service from 3D scan, Manufacturing, Prototyping, Bulk production and CAD service.

Later the website needs to have a multi language option.

Home:

1. Logo top left (attached)
2. Menu bar top right
3. Header picture like in the screenshot
4. Than the three small blue pics (CAD - Fertigung - Manufaktur) we want a
hoover-small zoom effect as soon as the mouse hits them.
5. Introduction text of our company
6. Contact Information (Design sample see attachment)
7. At the end "Impressum - Datenschutzerklärung - Haftungsausschluss. Those need to be linked to extra pages where we can add mandatory text (Legal notice, Privacy, Disclaimer)

Leistungen - Our service:

1. See the attachment named our service.
2. First on page a gallery where we can add pictures. If moving the mouse over the picture we want a one line explanation e.g. 3D Scan, Production, Die cast...
no click option at the pictures, just to see.
3. Below that, a side menu (we need to add or remove items by our self if necessary) on the left where we can add our service.
4. If the customer is clicking a service, it needs to be highlighted
5. After clicking a service we want our text to that service appear right of the menu (see attachment sample) and 2 big pictures on top of the menu and text field.

Gallery:

1. Headline pictures for each gallery Category (6-8 at the moment)
2. Mouse over the picture zooms it a little in and adds a text what category it is
e.g. Reverse engineering, Prototyping, Laserscan
3. Clicking on the picture opens the detail gallery to that category. There we need
to add pictures specific to that service.
4. If the customer is clicking on a picture from there, all pictures from that
Category will open in a full screen view mode

Blog:

1. A blog to add news (picture and text). Right now we don´t have the time to feed
it, so we want to deactivate it as long as we cant keep it up to date. Later it
should be part of the website.

Unternehmen:

1. Drop down menu: Our Team - History - Unsere Partner - AGB - Impressum

Our Team:
1. Short description of our employees including picture (see attachment)
2. Contact Information (Design sample see attachment)
3. At the end "Impressum - Datenschutzerklärung - Haftungsausschluss. Those need to be linked to extra pages where we can add mandatory text (Legal notice, Privacy, Disclaimer)

History:
1. Timeline where we can add milestones including date, and pictures of the company (see screenshot)

Unsere Partner:
1. Text field where we can introduce our partners including pictures if necessary.

A blog would be a nice option, social media shortcuts to Instagram-FB but no preview of FB Timeline within the website.

We do have professional text already, that will be added by us. We expect you to use any sample text and pictures for the draft, beside what we supply already.

If you see the need of buying pictures from Quorvane or any other picture company that is OK for us.

What we expect:

A modern, fresh website based on our existing design, changes are fine as long as the whole website design does not change completely to an unicorn thing in pink. Feel free to be creative. New ideas will be discussed, we are open to good ideas. We don´t stick fix to our idea, but we want our customers can see that its still the same company.
Scrolling effects would be a nice gadget if possible.

We have a bad page already...don´t want a second bad one :-)

Our company blue is RBG 106, 206, 224

Greets to all, looking for professional results.

Target Market(s)

B2B, Engineering companys,

Industry/Entity Type

Technical Service

Number of Pages Required

5+ page

Font styles to use
Sans Serif
Other font styles liked:
• verdana

Colors
0455a3
000000
ffffff

Requirements
Must have
• Responsive design, We want to be able to add posts to the Blog, pictures to the categories, and categories by ourself if necessary. (Wordpress)
• Lets say we want to add one more category at „Leistungen-Our Service“ that should be possible for us in the wordpress background.
Nice to have
• Dynamic elements to make the website more alive.
Should not have
• Sliders, Contact form

```html
<!DOCTYPE html>
<html lang="de">
<head>
<meta charset="utf-8">
<title>Norvek Precision</title>
<link rel="stylesheet" href="https://fonts.googleapis.com/css2?family=Raleway:wght@300;400;500;600&family=Open+Sans:wght@400;600&display=swap">
<style>
:root{
  --blue:#2fa8d8;
  --blue-deep:#0455a3;
  --navy:#1d2a44;
  --ink:#2b2f36;
  --muted:#6b7280;
  --paper:#ffffff;
  --mist:#eef0f2;
  --dark:#17191c;
}
*{box-sizing:border-box;margin:0;padding:0}
html,body{width:1200px;height:2372px;overflow:hidden}
body{font-family:"Open Sans",Verdana,sans-serif;color:var(--ink);background:var(--paper);position:relative}
.wordmark{font-family:"Raleway",sans-serif;font-weight:300;color:var(--ink);letter-spacing:4px;text-transform:uppercase;display:flex;align-items:center;gap:12px;white-space:nowrap}
.wordmark .dot{width:14px;height:14px;background:var(--blue);border-radius:50%}

/* header */
.site-header{position:absolute;top:0;left:0;width:1200px;height:130px;background:linear-gradient(#ffffff,#f3f4f5);border-bottom:1px solid #e2e4e7}
.site-header .wordmark{position:absolute;left:40px;top:48px;font-size:30px}
.main-nav{position:absolute;right:0;top:0;height:130px;display:flex;align-items:flex-start;padding-top:30px}
.main-nav::before{content:"";position:absolute;left:0;right:0;top:0;height:30px;background:var(--navy)}
.main-nav a{display:flex;align-items:center;justify-content:center;height:70px;padding:0 30px;font-family:"Raleway",sans-serif;font-size:16px;font-weight:500;color:var(--ink);text-decoration:none;letter-spacing:1px}
.main-nav a.active{background:var(--blue);color:#fff}
.main-nav .tail{width:30px;height:70px;background:var(--blue)}

/* hero */
.hero{position:absolute;top:130px;left:0;width:1200px;height:370px;background:linear-gradient(180deg,#f7f8f9,#dfe2e5)}
.hero-drawing{position:absolute;inset:0;background:radial-gradient(ellipse at 50% 60%,rgba(255,255,255,.7),rgba(200,205,210,.4))}
.hero .wordmark{position:absolute;left:360px;top:50px;font-size:64px;letter-spacing:6px}
.origin{position:absolute;top:160px;font-family:"Raleway",sans-serif;font-size:14px;font-weight:600;line-height:16px;display:flex;gap:10px;align-items:center;z-index:2}
.origin .flag{width:34px;height:40px;border-radius:2px}
.origin.de{left:360px}.origin.de .flag{background:linear-gradient(#111 33%,#d00 33% 66%,#f2c200 66%)}
.origin.as{left:700px}.origin.as .flag{background:#8a9099}
.hero-product{position:absolute;left:490px;top:150px;width:190px;height:180px;border-radius:20px;background:radial-gradient(circle,#c9ccd0,#8d939b 70%,transparent 71%)}
.pager{position:absolute;left:560px;top:340px;display:flex;gap:8px}
.pager span{width:8px;height:8px;border-radius:50%;background:#9aa0a6}
.pager span.on{background:#555}

/* services */
.services{position:absolute;top:500px;left:0;width:1200px;height:520px;background:radial-gradient(ellipse at 50% 40%,#3a3d42,#16181b 75%);clip-path:polygon(0 0,100% 0,100% 84%,50% 100%,0 84%)}
.service{position:absolute;text-align:center;color:#fff;font-family:"Raleway",sans-serif}
.service .ring{border-radius:50%;border:2px solid rgba(255,255,255,.35);background:radial-gradient(circle,rgba(47,168,216,.15),rgba(20,22,25,.6));display:flex;flex-direction:column;align-items:center;justify-content:center}
.service.small{top:115px;width:220px}
.service.small .ring{width:220px;height:220px}
.service.big{top:65px;left:445px;width:310px}
.service.big .ring{width:310px;height:310px;border-color:var(--blue);border-width:3px}
.service.cad{left:150px}.service.manu{left:830px}
.service h3{font-weight:400;font-size:22px;letter-spacing:1px;margin-top:10px}
.service.big h3{font-size:32px;color:#e9f6fb}
.service p{font-size:9px;letter-spacing:.5px;margin-top:6px;opacity:.85}
.service.big p{font-size:14px;letter-spacing:2px}

/* about */
.about{position:absolute;top:1060px;left:0;width:1200px;height:700px;background:linear-gradient(180deg,#ffffff,#eef0f2)}
.about-photo{position:absolute;left:620px;top:0;width:580px;height:560px;background:radial-gradient(ellipse at 55% 50%,#d4d7db,#9aa1a9 45%,#eef0f2 72%)}
.tag{position:absolute;left:120px;top:20px;background:var(--blue);color:#fff;font-family:"Raleway",sans-serif;font-size:13px;font-weight:600;letter-spacing:1px;padding:8px 18px}
.about h2{position:absolute;left:120px;top:70px;width:480px;font-family:"Raleway",sans-serif;font-weight:500;font-size:40px;line-height:48px;color:var(--blue);z-index:2}
.about .intro{position:absolute;left:120px;top:200px;width:430px;font-size:15px;line-height:23px;color:var(--muted)}
.btn{position:absolute;left:120px;top:505px;background:var(--blue);color:#fff;font-family:"Raleway",sans-serif;font-size:14px;font-weight:600;padding:14px 26px;letter-spacing:1px;display:flex;gap:14px;align-items:center}
.hotline{position:absolute;left:340px;top:510px;display:flex;gap:12px;align-items:center;font-family:"Raleway",sans-serif;font-weight:600;font-size:16px;white-space:nowrap}
.hotline .icon{width:40px;height:40px;border-radius:50%;background:var(--blue);display:flex;align-items:center;justify-content:center}

/* contact */
.contact{position:absolute;top:1760px;left:0;width:1200px;height:540px;background:#eceef0;text-align:center}
.contact .wordmark{justify-content:center;font-size:52px;margin-top:40px}
.contact h2{font-family:"Raleway",sans-serif;font-weight:400;font-size:38px;letter-spacing:3px;margin-top:34px}
.contact .sub{font-size:17px;color:var(--muted);margin-top:12px}
.cards{position:absolute;top:300px;left:150px;display:flex;gap:60px}
.card{width:260px;height:210px;background:#fff;box-shadow:0 6px 18px rgba(0,0,0,.12);padding-top:30px}
.card .icon{height:46px;display:flex;justify-content:center}
.card h4{font-family:"Raleway",sans-serif;font-size:16px;font-weight:600;color:var(--blue);letter-spacing:1px;margin-top:12px}
.card p{font-size:13px;line-height:19px;color:var(--ink);margin-top:14px}

/* footer */
.site-footer{position:absolute;top:2300px;left:0;width:1200px;height:72px;background:#dfe1e4;display:flex;justify-content:space-around;align-items:center;font-family:"Raleway",sans-serif;font-size:14px;font-weight:600;letter-spacing:1px}
.to-top{position:absolute;right:30px;top:2245px;width:40px;height:40px;background:#fff;box-shadow:0 2px 6px rgba(0,0,0,.2);display:flex;align-items:center;justify-content:center}
</style>
</head>
<body>

<header class="site-header">
  <div class="wordmark"><span class="dot"></span>Norvek Precision</div>
  <nav class="main-nav">
    <a class="active">HOME</a>
    <a>LEISTUNGEN</a>
    <a>GALERIE</a>
    <a>UNTERNEHMEN</a>
    <span class="tail"></span>
  </nav>
</header>

<section class="hero">
  <div class="hero-drawing" role="img" aria-label="Faint technical drawings in the background"></div>
  <div class="wordmark">Norvek Precision</div>
  <div class="origin de"><span class="flag"></span><span>MADE<br>IN<br>GERMANY</span></div>
  <div class="hero-product" role="img" aria-label="Exploded view of a precision machined assembly"></div>
  <div class="origin as"><span class="flag"></span><span>MADE<br>IN<br>ASIA</span></div>
  <div class="pager"><span class="on"></span><span></span><span></span></div>
</section>

<section class="services">
  <div class="service small cad">
    <div class="ring">
      <svg width="60" height="50" viewBox="0 0 60 50" fill="none" stroke="var(--blue)" stroke-width="4"><path d="M8 46 22 6 30 28 38 6 52 46"/><path d="M4 46h52"/></svg>
      <h3>CAD Service</h3>
      <p>3D-SCAN · REVERSE ENGINEERING</p>
    </div>
  </div>
  <div class="service big">
    <div class="ring">
      <svg width="90" height="64" viewBox="0 0 90 64" fill="none" stroke="var(--blue)" stroke-width="6"><circle cx="30" cy="36" r="16"/><circle cx="64" cy="20" r="11"/><circle cx="30" cy="36" r="5" fill="var(--blue)"/></svg>
      <h3>Fertigung</h3>
      <p>NATIONAL · INTERNATIONAL</p>
    </div>
  </div>
  <div class="service small manu">
    <div class="ring">
      <svg width="56" height="56" viewBox="0 0 56 56" fill="var(--blue)"><path d="M28 4 52 16v26L28 54 4 42V16z" opacity=".9"/><path d="M28 4 52 16 28 28 4 16z" fill="#8fd6ef"/></svg>
      <h3>Manufaktur</h3>
      <p>MODELLBAU · PROTOTYPEN</p>
    </div>
  </div>
</section>

<section class="about">
  <div class="about-photo" role="img" aria-label="Steel shaft coupling on a technical drawing"></div>
  <span class="tag">ABOUT US</span>
  <h2>Unsere Philosophie ist es, synergien zu nutzen.</h2>
  <p class="intro">Lorem Ipsum is simply dummy text of the printing and typesetting industry. Lorem Ipsum has been the industry's standard dummy text ever since the 1500s, when an unknown printer took a galley of type and scrambled it to make a type specimen book. It has survived not only five centuries, but also the leap into electronic typesetting, remaining essentially unchanged. It was popularised in the 1960s with the release of Letraset sheets containing Lorem Ipsum passages, and more recently with desktop publishing software including versions of Lorem Ipsum.</p>
  <span class="btn">READ MORE <svg width="16" height="10" viewBox="0 0 16 10" fill="none" stroke="#fff" stroke-width="2"><path d="M0 5h14M10 1l4 4-4 4"/></svg></span>
  <div class="hotline"><span class="icon"><svg width="18" height="18" viewBox="0 0 24 24" fill="#fff"><path d="M6.6 10.8a15 15 0 0 0 6.6 6.6l2.2-2.2a1 1 0 0 1 1-.25 11.4 11.4 0 0 0 3.6.57 1 1 0 0 1 1 1V20a1 1 0 0 1-1 1A17 17 0 0 1 3 4a1 1 0 0 1 1-1h3.5a1 1 0 0 1 1 1c0 1.25.2 2.45.57 3.57a1 1 0 0 1-.25 1z"/></svg></span>+49 (0) 1234/567-0</div>
</section>

<section class="contact">
  <div class="wordmark">Norvek Precision</div>
  <h2>KONTAKT</h2>
  <p class="sub">So erreichen uns</p>
  <div class="cards">
    <div class="card">
      <div class="icon"><svg width="34" height="46" viewBox="0 0 24 32" fill="var(--blue)"><path d="M12 0A12 12 0 0 0 0 12c0 9 12 20 12 20s12-11 12-20A12 12 0 0 0 12 0zm0 17a5 5 0 1 1 0-10 5 5 0 0 1 0 10z"/></svg></div>
      <h4>ADDRESS</h4>
      <p>88 Hallstatt Ring, Suite 12,<br>Neustadt 40210</p>
    </div>
    <div class="card">
      <div class="icon"><svg width="30" height="46" viewBox="0 0 20 32" fill="none" stroke="var(--blue)" stroke-width="2.5"><rect x="2" y="2" width="16" height="28" rx="3"/><path d="M8 26h4"/></svg></div>
      <h4>PHONE NUMBER</h4>
      <p>+49 (0) 1234/567-0<br>+49 (0) 1234/567-1</p>
    </div>
    <div class="card">
      <div class="icon"><svg width="46" height="46" viewBox="0 0 32 32" fill="none" stroke="var(--blue)" stroke-width="2.5"><rect x="2" y="7" width="28" height="19" rx="2"/><path d="M2 8l14 10L30 8"/></svg></div>
      <h4>EMAIL ADDRESS</h4>
      <p>info@norvek-precision.example</p>
    </div>
  </div>
</section>

<a class="to-top"><svg width="14" height="10" viewBox="0 0 14 10" fill="none" stroke="var(--ink)" stroke-width="2"><path d="M1 8l6-6 6 6"/></svg></a>

<footer class="site-footer">
  <span>IMPRESSUM</span>
  <span>DATENSCHUTZERKLÄRUNG</span>
  <span>HAFTUNGSAUSSCHLUSS</span>
</footer>

</body>
</html>
```